NEW YORK Plumbing/utility company 10 year anniversary business card

Looking For simple back and front business card would like to include a few things in description
We offer 24/7 emergency service
residential
commercial
industrial
municipal
services offered
Plumbing
hydro excavation
hydro jetting
Well pumps
Sewer pumps
water mains
sewer mains

```html
<!DOCTYPE html>
<html lang="en">
<head>
<meta charset="utf-8">
<title>Kestrel Water &amp; Sewer — Business Card</title>
<link rel="stylesheet" href="https://fonts.googleapis.com/css2?family=Red+Hat+Display:wght@400;500;700&display=swap">
<style>
  :root {
    --page-bg: #e4e4e4;
    --card-dark: #2d2b2a;
    --card-light: #f4f4f4;
    --brand-blue: #29a3dc;
    --brand-red: #e5232b;
    --brand-gray: #8a8a8a;
    --text-light: #ffffff;
  }
  * { margin: 0; padding: 0; box-sizing: border-box; }
  html, body { width: 1200px; height: 960px; overflow: hidden; }
  body {
    background: var(--page-bg);
    font-family: "Red Hat Display", Arial, sans-serif;
    position: relative;
  }
  .card {
    position: absolute;
    left: 297px;
    width: 606px;
    height: 346px;
    overflow: hidden;
  }
  .card--front { top: 113px; background: var(--card-dark); }
  .card--back { top: 512px; display: flex; }

  /* Front */
  .services {
    position: absolute; top: 28px; left: 0; right: 0;
    text-align: center; color: var(--text-light);
    font-size: 16px; line-height: 20px; font-weight: 400;
  }
  .services__label { color: var(--brand-blue); font-weight: 500; }
  .sep { color: var(--brand-red); margin: 0 4px; font-size: 10px; vertical-align: 2px; }
  .front-brand {
    position: absolute; top: 112px; left: 0; right: 0;
    display: flex; align-items: center; justify-content: center; gap: 16px;
    color: var(--brand-gray); font-weight: 700; font-size: 72px; letter-spacing: 1px;
  }
  .brand-dot { width: 38px; height: 38px; border-radius: 50%; background: var(--brand-blue); }
  .sectors {
    position: absolute; top: 285px; left: 0; right: 0;
    text-align: center; color: var(--text-light); font-size: 15px; letter-spacing: 0.2px;
  }
  .sector-dot {
    display: inline-block; width: 6px; height: 8px; margin: 0 4px 0 5px;
    background: var(--brand-blue); border-radius: 50% 50% 50% 50% / 60% 60% 40% 40%;
  }
  .emergency {
    position: absolute; top: 307px; left: 0; right: 0;
    text-align: center; color: var(--brand-red); font-size: 15px; font-weight: 700; letter-spacing: 0.3px;
  }

  /* Back */
  .back-brand {
    width: 303px; background: var(--card-light);
    display: flex; flex-direction: column; align-items: center; justify-content: center; gap: 10px;
  }
  .back-brand__dot { width: 30px; height: 30px; border-radius: 50%; background: var(--brand-blue); }
  .back-brand__name {
    color: var(--brand-red); font-weight: 700; font-size: 26px; line-height: 30px;
    text-align: center; letter-spacing: 0.5px;
  }
  .contact {
    flex: 1; background: var(--card-dark); position: relative; color: var(--text-light);
  }
  .contact__accent {
    position: absolute; left: 0; top: 86px; width: 12px; height: 37px; background: var(--brand-blue);
  }
  .contact__body { position: absolute; left: 44px; top: 84px; }
  .contact__name { color: var(--brand-red); font-size: 20px; font-weight: 700; line-height: 22px; }
  .contact__role { color: var(--brand-blue); font-size: 16px; line-height: 22px; }
  .contact__address { margin-top: 18px; font-size: 16px; line-height: 21px; }
  .contact__list { list-style: none; margin-top: 15px; font-size: 16px; line-height: 20px; }
  .contact__list li { display: flex; align-items: center; gap: 5px; }
  .contact__list svg { width: 14px; height: 14px; flex: none; }
</style>
</head>
<body>
  <section class="card card--front">
    <p class="services">
      <span class="services__label">Services Offered:</span> Plumbing<span class="sep">•</span>Hydro Excavation<span class="sep">•</span>Hydro Jetting<br>
      Well Pumps<span class="sep">•</span>Sewer Pumps<span class="sep">•</span>Water Mains<span class="sep">•</span>Sewer Mains
    </p>
    <div class="front-brand">
      <span class="brand-dot"></span>
      <span>Kestrel</span>
    </div>
    <p class="sectors">RESIDENTIAL<span class="sector-dot"></span>COMMERCIAL<span class="sector-dot"></span>INDUSTRIAL<span class="sector-dot"></span>MUNICIPAL</p>
    <p class="emergency">24/7 EMERGENCY SERVICE</p>
  </section>

  <section class="card card--back">
    <div class="back-brand">
      <span class="back-brand__dot"></span>
      <p class="back-brand__name">KESTREL<br>WATER &amp; SEWER</p>
    </div>
    <div class="contact">
      <span class="contact__accent"></span>
      <div class="contact__body">
        <p class="contact__name">Daniel Carver</p>
        <p class="contact__role">Founder / Owner</p>
        <p class="contact__address">P.O Box 418<br>Cedarfield, NY 10000</p>
        <ul class="contact__list">
          <li>
            <svg viewBox="0 0 16 16" aria-hidden="true"><path d="M4 1.5l2.2 3-1.3 1.6a8 8 0 0 0 5 5l1.6-1.3 3 2.2-1.2 2.3C8 14.5 1.5 8 1.7 2.7z" fill="none" stroke="#29a3dc" stroke-width="1.5" stroke-linejoin="round"/></svg>
            845-555-0142
          </li>
          <li>
            <svg viewBox="0 0 16 16" aria-hidden="true"><rect x="1.5" y="3.5" width="13" height="9" fill="none" stroke="#29a3dc" stroke-width="1.4"/><path d="M1.5 3.5l6.5 5 6.5-5" fill="none" stroke="#29a3dc" stroke-width="1.4"/></svg>
            daniel@kestrelws.com
          </li>
          <li>
            <svg viewBox="0 0 16 16" aria-hidden="true"><g fill="none" stroke="#29a3dc" stroke-width="1.2"><circle cx="8" cy="8" r="6.3"/><ellipse cx="8" cy="8" rx="2.8" ry="6.3"/><path d="M1.7 8h12.6M2.6 5h10.8M2.6 11h10.8"/></g></svg>
            www.kestrelws.com
          </li>
        </ul>
      </div>
    </div>
  </section>
</body>
</html>
```